TELURIN WEB DESIGN (please use the uploaded photos)

We are looking for a web design that captures the essence of Telurin: authenticity, connection with nature, and simplicity. We want the page to convey the story of our brand, from its cultural significance to its commitment to quality and authenticity. Additionally, we need to integrate Telurin's sub-brands, such as BOSRE, our line of healthy pecan nut snacks.

Design Objective:
We want our website to be more than just a product showcase: it should be a reflection of our brand identity and a platform that inspires our customers to connect with us on a deeper level.

Company Background:
Telurin is a company specializing in walnut production, hunting ranch management, and livestock. The name "Telurin" means "FOUR" in the PIMA dialect, in honor of the Pima communities that once inhabited the ranch. This historical and cultural connection is at the heart of our brand.

Audience Needs and Aspirations:
All our customers share deep emotional needs. They seek authenticity, honesty, and a happy, simple life. They want to reconnect with their natural state, dream, return to simplicity, and renew their hopes.

Brand Archetype:
Inspired by the archetypes of Greta, Tobias Wrenfield, and Innocent, we aim to reflect the need to be oneself, honesty, and authenticity in all aspects.

Brand Objective:
Our mission is to reconnect our customers with their natural state, offering high-quality products that simplify their lives and inspire them to dream and renew their hopes.

Key Design Elements:

Natural and earthy color palette reflecting our connection to nature.
Images and graphics depicting ranch life, walnut production, and the quality of our products.
Clean and easy-to-navigate design to reflect our philosophy of simplicity and honesty.
Seamless and clear integration of sub-brands, such as BOSRE.

Target Market(s)

Organic Women (30-50 years) committed to exercise and healthy diets. Hunters (40-60 years) with a deeply rooted conservative mindset. Prime Men (40-60 years) with high income, power, and status.

Coding

Coded - Design and coding required

Number of Pages Required

4 page

Other font styles liked:
• Brother 1816 Printed

Requirements
Must have
• Authenticity and Nature Connection: Reflect the brand's authenticity and connection to nature through design elements. Simplicity and Navigation: Keep the design clean and easy to navigate. Integration of Sub-brands: Seamlessly incorporate sub-brands like BOSRE into the design. Quality Imagery: Use high-quality visuals to showcase products and brand essence. Responsive Design: Ensure the website looks and functions well across different devices. Storytelling: Incorporate storytelling to convey the brand's history, values, and culture. Clear CTAs: Include clear calls-to-action to guide visitors towards desired actions.
Nice to have
• I have the telurinhq.com Domain, also I'm working on WIX

```html
<!DOCTYPE html>
<html lang="en">
<head>
<meta charset="utf-8">
<title>Telurin — We Believe in the Power of Nature</title>
<link rel="stylesheet" href="https://fonts.googleapis.com/css2?family=Josefin+Sans:wght@400;600&family=Mulish:wght@400;600;700&display=swap">
<style>
  :root {
    --orange: #ec6a37;
    --orange-deep: #d4582a;
    --ink: #1f1c1a;
    --text: #3c3835;
    --white: #ffffff;
    --footer: #1d1c1b;
    --brown: #33241b;
    --field-dark: #3b3a22;
    --field-green: #5f7a2c;
    --corn: #7e9a3c;
  }
  * { box-sizing: border-box; margin: 0; padding: 0; }
  html, body { width: 1200px; height: 3094px; overflow: hidden; }
  body { position: relative; background: var(--white); font-family: "Mulish", sans-serif; color: var(--text); }
  .abs { position: absolute; }
  .heading { font-family: "Josefin Sans", sans-serif; font-weight: 400; text-transform: uppercase; line-height: 1.1; }
  .eyebrow { font-family: "Josefin Sans", sans-serif; font-size: 15px; letter-spacing: .5px; text-transform: uppercase; color: var(--orange); }
  .btn { display: flex; align-items: center; justify-content: center; font-family: "Mulish", sans-serif; font-weight: 700; font-size: 15px; letter-spacing: .6px; text-transform: uppercase; }

  /* Header */
  .site-header { left: 0; top: 0; width: 1200px; height: 78px; background: rgba(35,30,26,.82); z-index: 3; }
  .brand { display: flex; align-items: center; gap: 8px; font-family: "Josefin Sans", sans-serif; font-size: 30px; color: var(--white); letter-spacing: 1px; }
  .brand-mark { width: 16px; height: 16px; background: var(--orange); }
  .site-header .brand { left: 139px; top: 27px; }
  .nav-link { font-size: 13px; font-weight: 600; letter-spacing: .4px; color: var(--white); text-transform: uppercase; top: 31px; }
  .nav-link.is-active { font-weight: 700; }
  .nav-underline { left: 479px; top: 54px; width: 66px; height: 1px; background: var(--white); }

  /* Hero */
  .hero-photo { left: 0; top: 0; width: 1200px; height: 745px;
    background: linear-gradient(100deg, #2f2c1d 0%, #4a4726 32%, #5d6a2c 52%, #6f8a34 72%, #8aa04a 100%); }
  .hero-field { left: 0; top: 420px; width: 1200px; height: 325px;
    background: linear-gradient(180deg, rgba(80,110,40,0) 0%, rgba(74,104,34,.7) 60%, rgba(60,90,28,.9) 100%); }
  .hero-title { left: 128px; top: 246px; font-size: 53px; color: var(--white); }
  .hero-text { left: 134px; top: 368px; width: 400px; font-size: 18px; line-height: 27px; color: var(--white); }
  .hero-cta { left: 138px; top: 468px; width: 185px; height: 50px; background: var(--orange); color: var(--white); }
  .hero-curve { left: 0; top: 640px; }

  /* About */
  .about-ring { left: 126px; top: 755px; width: 440px; height: 440px; border-radius: 50%; background: var(--orange); }
  .about-photo { left: 150px; top: 780px; width: 414px; height: 414px; border-radius: 50%; border: 4px solid var(--white);
    background: radial-gradient(circle at 55% 45%, #d9b53a 0%, #9c7a34 35%, #6d5035 65%, #4a3a2e 100%); }
  .about-eyebrow { left: 611px; top: 780px; }
  .about-title { left: 611px; top: 800px; font-size: 46px; color: var(--ink); }
  .about-text { left: 615px; top: 878px; width: 478px; font-size: 16px; line-height: 26.5px; color: var(--text); }
  .about-cta { left: 617px; top: 1097px; width: 174px; height: 46px; border: 2px solid var(--orange); color: var(--orange); }

  /* Vision / Mission */
  .panel { top: 1263px; height: 462px; color: var(--white); text-align: center; }
  .panel-vision { left: 0; width: 605px; background: radial-gradient(ellipse at 50% 30%, #4a3527 0%, var(--brown) 70%); }
  .panel-mission { left: 605px; width: 595px; background: radial-gradient(ellipse at 50% 40%, #e0663a 0%, var(--orange-deep) 75%); }
  .panel-title { position: absolute; left: 0; right: 0; top: 162px; font-size: 38px; }
  .panel-text { position: absolute; left: 50%; transform: translateX(-50%); top: 212px; width: 420px; font-size: 18px; line-height: 28px; }

  /* Products */
  .products-eyebrow { left: 0; width: 1200px; top: 1786px; text-align: center; }
  .products-title { left: 0; width: 1200px; top: 1810px; text-align: center; font-size: 46px; color: var(--ink); }
  .product-card { top: 1900px; width: 287px; height: 371px; border-radius: 50%; overflow: hidden; color: var(--white); text-align: center; }
  .product-oil { left: 135px; background: linear-gradient(180deg, #b9a35a 0%, #8a7330 45%, #4a3c22 75%, #222 100%); }
  .product-beauty { left: 474px; background: linear-gradient(180deg, #6d5a5a 0%, #4c3b37 35%, #3a2d28 60%, #1f1c1b 100%); }
  .product-flour { left: 813px; background: linear-gradient(180deg, #2a2624 0%, #8b7866 35%, #bdb8b2 65%, #2a2826 100%); }
  .product-ring { left: 466px; top: 1889px; width: 303px; height: 391px; border-radius: 50%; border: 2px solid var(--orange); }
  .product-label { position: absolute; left: 0; right: 0; font-size: 25px; }
  .product-oil .product-label { top: 290px; }
  .product-flour .product-label { top: 274px; }
  .product-beauty .product-label { top: 108px; font-size: 23px; line-height: 28px; }
  .product-note { position: absolute; left: 0; right: 0; top: 182px; font-size: 11.5px; line-height: 20px; }
  .product-cta { position: absolute; left: 83px; top: 243px; width: 124px; height: 31px; background: var(--orange); color: var(--white); font-size: 10px; }

  /* Reconnect */
  .reconnect-photo { left: 560px; top: 2363px; width: 640px; height: 535px;
    background: radial-gradient(ellipse at 60% 55%, #b8693a 0%, #8a4a26 45%, #4d3022 80%, #d8c7a3 100%); }
  .reconnect-shape { left: 0; top: 2363px; }
  .reconnect-eyebrow { left: 148px; top: 2498px; color: var(--white); }
  .reconnect-title { left: 148px; top: 2521px; font-size: 41px; line-height: 51px; color: var(--white); }
  .reconnect-text { left: 148px; top: 2627px; width: 420px; font-size: 16px; line-height: 26.5px; color: var(--white); }
  .reconnect-cta { left: 145px; top: 2724px; width: 175px; height: 46px; background: var(--ink); color: var(--white); }

  /* Footer */
  .site-footer { left: 0; top: 2898px; width: 1200px; height: 196px; background: var(--footer); }
  .site-footer .brand { left: 160px; top: 56px; }
  .footer-link { top: 66px; font-size: 13px; font-weight: 600; letter-spacing: .4px; color: var(--white); text-transform: uppercase; }
  .footer-rule { left: 0; top: 116px; width: 1200px; height: 1px; background: #3a3836; }
  .copyright { left: 166px; top: 150px; font-size: 11px; color: #d8d6d3; }
  .social { top: 128px; width: 26px; height: 26px; border-radius: 50%; border: 1.5px solid var(--white); }
</style>
</head>
<body>

<!-- Hero -->
<div class="abs hero-photo" role="img" aria-label="Photo of a green cornfield at sunset beside a mown meadow"></div>
<div class="abs hero-field"></div>

<header class="abs site-header">
  <div class="abs brand"><span class="brand-mark"></span>TELURIN</div>
  <span class="abs nav-link is-active" style="left:479px">About us</span>
  <span class="abs nav-underline"></span>
  <span class="abs nav-link" style="left:605px">Products</span>
  <span class="abs nav-link" style="left:739px">BOSRE</span>
  <span class="abs nav-link" style="left:841px">Blogs</span>
  <span class="abs nav-link" style="left:948px">Contact us</span>
</header>

<h1 class="abs heading hero-title">We believe in the<br><span style="font-weight:600">power of nature</span></h1>
<p class="abs hero-text">We are a family-owned business dedicated to agriculture, which focuses on cultivating the Sonora region's pecan tree.</p>
<a class="abs btn hero-cta">Learn more</a>

<svg class="abs" style="left:514px;top:574px" width="172" height="70" viewBox="0 0 172 70" aria-hidden="true">
  <path d="M2 68 A86 86 0 0 1 170 68" fill="none" stroke="#ffffff" stroke-width="1.2"/>
  <path d="M88 28 V60 M78 50 L88 60 L98 50" fill="none" stroke="#ffffff" stroke-width="1.6"/>
</svg>

<svg class="abs hero-curve" width="1200" height="106" viewBox="0 0 1200 106" aria-hidden="true">
  <path d="M0 106 Q600 -28 1200 106 Z" fill="#ec6a37"/>
  <path d="M0 106 Q600 -4 1200 106 Z" fill="#ffffff"/>
</svg>

<!-- About -->
<div class="abs about-ring"></div>
<div class="abs about-photo" role="img" aria-label="Photo of a bottle of pecan oil with bread, pecans and a jar on a wooden board"></div>
<span class="abs eyebrow about-eyebrow">Who we are</span>
<h2 class="abs heading about-title">About us</h2>
<p class="abs about-text">We are a family-owned business dedicated to agriculture, which focuses on cultivating the Sonora region's pecan tree. Our goal is to create authentic products that harness the natural benefits of pecans. We believe in connecting with the land and using sustainable practices to grow pecan trees in the fertile soil of Sonora. This allows us to offer high-quality products that showcase the pure goodness of pecans.</p>
<a class="abs btn about-cta">Learn more</a>

<!-- Vision / Mission -->
<section class="abs panel panel-vision" role="img" aria-label="Photo of a smiling woman applying oil with a dropper, under a dark brown tint">
  <h2 class="heading panel-title">Our vision</h2>
  <p class="panel-text">To be a company that develops authentic products, services, and experiences that help reconnect with your natural state.</p>
</section>
<section class="abs panel panel-mission" role="img" aria-label="Close-up photo of pecan halves under an orange tint">
  <h2 class="heading panel-title">Our mission</h2>
  <p class="panel-text">Create innovative products and services that guide individuals toward rediscovering their true purpose.</p>
</section>

<!-- Products -->
<span class="abs eyebrow products-eyebrow">What we offer</span>
<h2 class="abs heading products-title">Our produts</h2>

<div class="abs product-ring"></div>
<div class="abs product-card product-oil" role="img" aria-label="Photo of rows of pecan oil bottles">
  <span class="heading product-label">Pecan oil</span>
</div>
<div class="abs product-card product-beauty" role="img" aria-label="Photo of dropper bottles of pecan oil beauty products on pecan shells">
  <span class="heading product-label">Beauty products<br>pecan oil based</span>
  <p class="product-note">Unique beauty product line based on<br>the benefits of pecan</p>
  <a class="btn product-cta">Learn more</a>
</div>
<div class="abs product-card product-flour" role="img" aria-label="Photo of hands sifting pecan flour">
  <span class="heading product-label">Pecan flour</span>
</div>

<!-- Reconnect -->
<div class="abs reconnect-photo" role="img" aria-label="Photo of a pile of pecans, walnuts and almonds"></div>
<svg class="abs reconnect-shape" width="660" height="535" viewBox="0 0 660 535" aria-hidden="true">
  <path d="M0 0 H585 C640 60 660 150 640 240 C620 330 575 420 566 535 H0 Z" fill="#ec6a37"/>
  <path d="M585 0 C640 60 660 150 640 240 C620 330 575 420 566 535" fill="none" stroke="#ffffff" stroke-width="6"/>
</svg>
<span class="abs eyebrow reconnect-eyebrow">Who we are</span>
<h2 class="abs heading reconnect-title">Reconnect with<br>your natural state</h2>
<p class="abs reconnect-text">Lorem ipsum dolor sit amet, consectetur adipiscing elit, sed do eiusmod tempor incididunt ut labore et dolore magna aliqua. Ut enim ad minim veniam</p>
<a class="abs btn reconnect-cta">Learn more</a>

<!-- Footer -->
<footer class="abs site-footer">
  <div class="abs brand"><span class="brand-mark"></span>TELURIN</div>
  <span class="abs footer-link" style="left:453px">About us</span>
  <span class="abs footer-link" style="left:578px">Products</span>
  <span class="abs footer-link" style="left:711px">BOSRE</span>
  <span class="abs footer-link" style="left:813px">Blogs</span>
  <span class="abs footer-link" style="left:920px">Contact us</span>
  <div class="abs footer-rule"></div>
  <p class="abs copyright">© 2024 Company Name &nbsp;All Rights Reserved</p>
  <span class="abs social" style="left:917px" aria-label="Social link"></span>
  <span class="abs social" style="left:950px" aria-label="Social link"></span>
  <span class="abs social" style="left:984px" aria-label="Social link"></span>
</footer>

</body>
</html>
```